Certificate of Completion for a Trustee of a Christian School after having taken an online traini...

We need an exceptionally professional certificate of completion that can be downloaded / printed off and displayed on an office wall and/or presented as part of an accreditation process for a school. Attached is a very rough idea of the content.

```html
<!DOCTYPE html>
<html lang="en">
<head>
<meta charset="utf-8">
<title>Harbourlight Schools Network – Strategic Leader Certificate</title>
<link href="https://fonts.googleapis.com/css2?family=Mulish:wght@400;500;600&family=Noto+Serif:wght@400&display=swap" rel="stylesheet">
<style>
  :root {
    --paper: #ffffff;
    --edge: #9a9a9a;
    --ink: #1f1f1f;
    --brand: #2b78b0;
    --gold: #d9a441;
    --gold-soft: #f3dfb4;
    --rule: #8a8a8a;
  }
  * { margin: 0; padding: 0; box-sizing: border-box; }
  html, body { width: 1200px; height: 848px; overflow: hidden; background: var(--paper); }
  body { font-family: "Mulish", Arial, sans-serif; color: var(--ink); }

  .certificate {
    position: relative;
    width: 1200px; height: 848px;
    border: 2px solid var(--edge);
    background: radial-gradient(ellipse at 50% 45%, #ffffff 0%, #fbfbfc 60%, #f4f5f7 100%);
    overflow: hidden;
  }

  .corner {
    position: absolute;
    width: 112px; height: 112px;
    background: radial-gradient(circle closest-side at var(--cx) var(--cy), rgba(217,164,65,.85) 0%, rgba(243,223,180,.6) 55%, rgba(255,255,255,0) 100%);
  }
  .corner--tl { top: 30px; left: 34px; --cx: 30%; --cy: 30%; }
  .corner--tr { top: 30px; right: 34px; --cx: 70%; --cy: 30%; }
  .corner--bl { bottom: 30px; left: 34px; --cx: 30%; --cy: 70%; }
  .corner--br { bottom: 30px; right: 34px; --cx: 70%; --cy: 70%; }

  .centered { position: absolute; left: 0; width: 100%; text-align: center; }

  .brand {
    top: 122px;
    font-size: 30px; font-weight: 500;
    color: var(--brand); line-height: 1;
  }
  .program { top: 206px; font-size: 20px; font-weight: 500; }
  .level-label { top: 258px; font-size: 19px; }
  .level-title {
    top: 288px; font-size: 37px; font-weight: 500; color: var(--brand);
    display: flex; justify-content: center; align-items: center; gap: 18px;
  }
  .level-title .marker {
    display: inline-block; width: 14px; height: 14px;
    background: var(--brand);
    transform: rotate(45deg);
  }
  .name-label { top: 354px; font-size: 19px; }
  .recipient {
    top: 388px; font-family: "Noto Serif", Georgia, serif;
    font-size: 58px; color: var(--brand); line-height: 1.1;
  }
  .name-rule {
    position: absolute; top: 450px; left: 306px; width: 602px;
    border-top: 1px dashed var(--rule);
  }

  .fields {
    position: absolute; top: 490px; left: 137px; width: 960px;
    display: grid; grid-template-columns: 141px 313px 60px 133px 313px;
    row-gap: 10px; font-size: 17px;
  }
  .field-line { border-bottom: 1.5px dotted #555; height: 16px; }

  .scripture { top: 572px; font-size: 17px; line-height: 23px; }
  .scripture .highlight { color: var(--brand); font-weight: 600; }
  .reference { top: 658px; font-size: 17px; }

  .terms { top: 728px; font-size: 10.5px; line-height: 15.5px; }
</style>
</head>
<body>
<main class="certificate">
  <div class="corner corner--tl" role="img" aria-label="Gold filigree corner ornament"></div>
  <div class="corner corner--tr" role="img" aria-label="Gold filigree corner ornament"></div>
  <div class="corner corner--bl" role="img" aria-label="Gold filigree corner ornament"></div>
  <div class="corner corner--br" role="img" aria-label="Gold filigree corner ornament"></div>

  <p class="centered brand">Harbourlight Schools Network</p>
  <p class="centered program">Faith School Stewardship</p>

  <p class="centered level-label">Level One:</p>
  <h1 class="centered level-title">
    <span class="marker" aria-hidden="true"></span>
    Strategic Leader
    <span class="marker" aria-hidden="true"></span>
  </h1>

  <p class="centered name-label">Name:</p>
  <p class="centered recipient">Daniel Morrow</p>
  <div class="name-rule"></div>

  <div class="fields">
    <span>Year:</span><span class="field-line"></span><span></span><span>State:</span><span class="field-line"></span>
    <span>School Name:</span><span class="field-line"></span><span></span><span>Association:</span><span class="field-line"></span>
  </div>

  <p class="centered scripture">
    Posterity will serve him; future generations will be told about the Lord.<br>
    They will proclaim his righteousness, declaring to a people yet unborn:<br>
    <span class="highlight">He has done it!</span>
  </p>
  <p class="centered reference">Psalm 22: 30-31</p>

  <p class="centered terms">
    This certificate qualifies the Trustee in meeting Harbourlight Governance Standards for one year. The Trustee<br>
    must take an additional module each year in order to continue to meet Harbourlight Governance standards.<br>
    It may also qualify for your Association's accreditation standards.
  </p>
</main>
</body>
</html>
```